Design Brief: Tidewell Group Business Card Design
Project Overview

Tidewell Group is a strategic partner to entrepreneurs and leadership teams, supporting business growth through clarity, execution, and trusted expertise. We are looking for a premium, modern business card design that reflects confidence, professionalism, and upward momentum.

Main logo the one with gold bar for the Tidewell Group.

This card will be used by executives and staff across the Tidewell Group business.

Brand Personality
Professional but human
Confident but collaborative
Strategic, credible, and execution-focused
Premium without being flashy

This is not a startup, tech gimmick, or overly creative brand.

Card Format
Portrait orientation (vertical)
Standard size: 55 × 90 mm
Two-sided
One corner cut (top-right corner preferred) to subtly represent upward movement and growth

Design must still work if corner cutting is not available with certain printers

Front Side (Contact Details)
Include:
Tidewell Group logo (provided)
Name
Title
Phone number
Email address
Website
Optional: tagline at the bottom

Style:
Clean
Minimal
Plenty of white space
Easy to read

Back Side (Ecosystem / Brand Message)
Include:
Heading such as: “The Tidewell Network”
Short 2–3 line description explaining that Tidewell is a strategic partner with an ecosystem of specialist professional services businesses operating across Strategic Advisory, Capital Raising, People, & Finance.

This side should reinforce scale, capability, and partnership, not sales messaging.

Colours
Primary brand colours:
Tidewell Blue: #0063B0
Deep Blue: #1A3D6D
Gold accent (very subtle use only): #C9A24D

Rules:
No gradients
No bright or neon colours
No heavy textures
Gold should be minimal and refined

Typography
Clean, modern sans-serif
Professional and readable
No script or decorative fonts

What to Avoid
Landscape layouts (Unless recommended based on logo design, which is horizontal in nature)
Overdesigned or cluttered cards
Loud colours or gradients
Trendy effects that won’t age well

Multiple accent colours

Deliverables
Print-ready files (PDF)
Editable source files (AI / PSD)
Front and back designs

Mockups showing the portrait card and cut corner

Target Outcome
A business card that feels:
Executive
Distinctive
Timeless
Aligned to a strategic, multi-division business

Target Market(s)

Business Owners and Executives (Across industries)

Industry/Entity Type

Professional Services

Contact Information for Business Card

First name and Surname, Email address, Cell phone number, website

Font styles to use
Other font styles liked:
• IBM Plex Sans and or Sans Pro

Colors
0054AA
0677BA
7BADD7
CADEEF
E8F1F8

Requirements
Must have
• Include QR code to digital business card.

```html
<!DOCTYPE html>
<html lang="en">
<head>
<meta charset="utf-8">
<title>Tidewell Group – Business Card, Front and Back</title>
<link rel="stylesheet" href="https://fonts.googleapis.com/css2?family=Open+Sans:ital,wght@0,400;0,600;0,700;1,400&family=Source+Serif+4:wght@600;700&display=swap">
<style>
  :root {
    --tidewell-blue: #0063B0;
    --deep-blue: #1A3D6D;
    --navy-card: #1F3A68;
    --gold: #C9A24D;
    --ink: #1E2633;
    --ink-soft: #3A4250;
    --paper: #FFFFFF;
    --canvas: #ECEEF1;
  }
  * { box-sizing: border-box; margin: 0; padding: 0; }
  html, body {
    width: 800px; height: 1200px; overflow: hidden;
    background: var(--canvas);
  }
  .sheet {
    width: 800px; height: 1200px;
    display: flex; align-items: center; justify-content: center; gap: 30px;
  }
  .card {
    position: relative;
    width: 360px; height: 589px;
    border-radius: 10px;
    overflow: hidden;
    box-shadow: 0 4px 14px rgba(20, 30, 50, 0.12);
  }

  /* Back side */
  .card-back {
    background: var(--navy-card);
    color: #FFFFFF;
    padding: 130px 34px 0 34px;
    font-family: "Open Sans", sans-serif;
  }
  .back-heading {
    font-family: "Source Serif 4", serif;
    font-weight: 700;
    font-size: 33px;
    line-height: 1.1;
    color: var(--gold);
    margin-bottom: 24px;
  }
  .back-description {
    font-size: 15.5px;
    line-height: 1.55;
    margin-bottom: 30px;
  }
  .back-description strong { font-weight: 600; }
  .service-list { list-style: none; }
  .service-list li {
    font-size: 19px;
    line-height: 1.9;
    display: flex; align-items: center; gap: 12px;
  }
  .service-list li::before {
    content: ""; width: 6px; height: 6px; border-radius: 50%;
    background: var(--gold);
  }
  .qr-code {
    position: absolute; right: 34px; bottom: 36px;
    width: 84px; height: 84px;
    background: var(--paper);
    border-radius: 4px;
    padding: 8px;
  }
  .qr-code-field {
    width: 100%; height: 100%;
    border: 3px solid var(--deep-blue);
  }

  /* Front side */
  .card-front {
    background: var(--paper);
    clip-path: polygon(0 0, calc(100% - 44px) 0, 100% 44px, 100% 100%, 0 100%);
    font-family: "Open Sans", sans-serif;
    color: var(--ink);
  }
  .corner-accent {
    position: absolute; top: 0; right: 0;
    width: 64px; height: 64px;
    background: var(--gold);
    clip-path: polygon(20px 0, 100% 64px, 100% 44px, 44px 0);
  }
  .brand {
    position: absolute; top: 66px; left: 34px;
    display: flex; align-items: center; gap: 14px;
  }
  .brand-square {
    width: 44px; height: 44px; background: var(--deep-blue);
  }
  .brand-name {
    font-family: "Open Sans", sans-serif;
    font-weight: 700;
    font-size: 33px;
    line-height: 1.02;
    letter-spacing: 0.5px;
    text-transform: uppercase;
    color: var(--ink);
  }
  .person {
    position: absolute; top: 225px; left: 34px;
  }
  .person-name {
    font-family: "Source Serif 4", serif;
    font-weight: 600;
    font-size: 29px;
    color: var(--ink);
  }
  .person-title {
    font-size: 17px;
    color: var(--deep-blue);
    margin-top: 2px;
  }
  .contact-list {
    position: absolute; top: 330px; left: 34px;
    list-style: none;
  }
  .contact-list li {
    display: flex; align-items: center; gap: 16px;
    font-size: 16.5px; color: var(--ink-soft);
    height: 40px;
  }
  .contact-icon { width: 20px; height: 20px; flex: none; }
  .tagline {
    position: absolute; top: 478px; left: 34px; right: 30px;
    font-style: italic;
    font-size: 15.5px;
    line-height: 1.45;
    color: var(--ink-soft);
  }
  .base-band {
    position: absolute; left: 0; right: 0; bottom: 0;
    height: 28px; background: var(--deep-blue);
  }
</style>
</head>
<body>
<main class="sheet">

  <section class="card card-back" aria-label="Card back">
    <h2 class="back-heading">The Tidewell<br>Network</h2>
    <p class="back-description">
      Tidewell is your strategic partner with an ecosystem of specialist professional services businesses operating across
      <strong>Strategic Advisory, Capital Raising, People, &amp; Finance.</strong>
    </p>
    <ul class="service-list">
      <li>Strategic Advisory</li>
      <li>Capital Raising</li>
      <li>People</li>
      <li>Finance</li>
    </ul>
    <div class="qr-code" role="img" aria-label="QR code linking to the digital business card">
      <div class="qr-code-field"></div>
    </div>
  </section>

  <section class="card card-front" aria-label="Card front">
    <div class="corner-accent"></div>

    <div class="brand">
      <span class="brand-square"></span>
      <span class="brand-name">Tidewell<br>Group</span>
    </div>

    <div class="person">
      <h1 class="person-name">Elena Varga</h1>
      <p class="person-title">Managing Partner</p>
    </div>

    <ul class="contact-list">
      <li>
        <svg class="contact-icon" viewBox="0 0 24 24" aria-hidden="true">
          <path fill="#1E2633" d="M6.6 10.8a15.2 15.2 0 0 0 6.6 6.6l2.2-2.2a1 1 0 0 1 1-.25 11.4 11.4 0 0 0 3.6.57 1 1 0 0 1 1 1V20a1 1 0 0 1-1 1A17 17 0 0 1 3 4a1 1 0 0 1 1-1h3.5a1 1 0 0 1 1 1c0 1.25.2 2.45.57 3.570a1 1 0 0 1-.25 1z"/>
        </svg>
        (555) 214-3308
      </li>
      <li>
        <svg class="contact-icon" viewBox="0 0 24 24" aria-hidden="true">
          <rect x="2" y="5" width="20" height="14" rx="1.5" fill="#1A3D6D"/>
          <path d="M2.5 6l9.5 7 9.5-7" fill="none" stroke="#FFFFFF" stroke-width="1.6"/>
        </svg>
        elena@tidewellgroup.com
      </li>
      <li>
        <svg class="contact-icon" viewBox="0 0 24 24" aria-hidden="true">
          <g fill="none" stroke="#1A3D6D" stroke-width="1.8">
            <circle cx="12" cy="12" r="9.5"/>
            <ellipse cx="12" cy="12" rx="4" ry="9.5"/>
            <path d="M2.5 12h19"/>
          </g>
        </svg>
        www.tidewellgroup.com
      </li>
    </ul>

    <p class="tagline">Partnering Vision. Accelerating Growth. Empowering Execution.</p>

    <div class="base-band"></div>
  </section>

</main>
</body>
</html>
```